Marlowe Chiropractic Business card

Health related business card, picture on front, logo on back with a spot to schedule multiple appointments.
address, website, email, name of the clinic, chiropractic physician, www.MarloweChiropractic-example.com P) 555-482-1963 F)555-482-7751, Drtedmarlowe@mailbox-example.com, 487 Keswick lane Suite 208., Nashville, TN 48302. I would like for it to be professional, with a slight fun and healthy attitude

Industry/Entity Type

Health Care

Contact Information for Business Card

Health related business card, picture on front, logo on back with appointment times.
address, website, email, name of the clinic, chiropractic physician, www.MarloweChiropractic-example.com P) 555-482-1963 F)555-482-7751, Drtedmarlowe@mailbox-example.com, 487 Keswick lane Suite 208., Nashville, TN 48302

Font styles to use
Sans Serif

Colors
3176b5
33b8a4
0255a3
00a990
feeeee

Requirements
Must have
• Dr. Ted Marlowe, or Ted Marlowe, D.C., I want rounded corners, picture on front

```html
<!DOCTYPE html>
<html lang="en">
<head>
<meta charset="utf-8">
<title>Marlowe Chiropractic – Business Card</title>
<link rel="stylesheet" href="https://fonts.googleapis.com/css2?family=Cinzel:wght@600;700&family=Jost:wght@300;400&family=Source+Sans+3:ital,wght@0,400;1,400&display=swap">
<style>
  :root {
    --stage: #3b3b3b;
    --brand-blue: #0f4fa0;
    --brand-green: #7ab23a;
    --band-blue: #0d51a1;
    --band-green: #76b83c;
    --ink: #3d3d3d;
    --ink-soft: #5a5f66;
    --front-paper: #f7f7f7;
    --back-paper: #dde6ee;
    --rule: #4a4f55;
  }
  * { box-sizing: border-box; margin: 0; padding: 0; }
  html, body { width: 1200px; height: 750px; overflow: hidden; }
  body { background: var(--stage); position: relative; }

  .card {
    position: absolute;
    top: 228px;
    width: 461px;
    height: 262px;
    border-radius: 14px;
    overflow: hidden;
  }
  .card--front { left: 124px; background: var(--front-paper); }
  .card--back { left: 618px; background: var(--back-paper); }

  /* brand name in place of the mark */
  .brand {
    position: absolute;
    font-family: "Cinzel", serif;
    font-weight: 700;
    color: var(--brand-blue);
    font-size: 19px;
    line-height: 1.05;
    letter-spacing: 0.2px;
    display: flex;
    align-items: center;
    gap: 8px;
  }
  .brand__dot { width: 14px; height: 14px; border-radius: 50%; background: var(--brand-blue); flex: none; }
  .card--front .brand { left: 22px; top: 22px; }
  .card--back .brand { right: 42px; top: 22px; text-align: right; }

  .person {
    position: absolute; left: 22px; top: 85px;
    font-family: "Cinzel", serif;
  }
  .person__name { font-weight: 600; font-size: 17px; color: var(--brand-blue); letter-spacing: 0.3px; }
  .person__title { font-weight: 600; font-size: 12.5px; color: var(--brand-green); letter-spacing: 0.4px; margin-top: 1px; }

  .contact {
    position: absolute; left: 23px; top: 133px;
    font-family: "Jost", sans-serif; font-weight: 300;
    font-size: 12px; color: var(--ink); line-height: 17.5px;
    list-style: none;
  }
  .contact__line { display: flex; align-items: center; gap: 5px; white-space: nowrap; }
  .contact__icon { width: 12px; height: 12px; flex: none; }

  .portrait {
    position: absolute; left: 266px; top: 8px; width: 195px; height: 236px;
    background: linear-gradient(180deg, #f4f4f4 0%, #d9cfc8 35%, #b9c6d2 65%, #9fb0c2 100%);
  }

  .band { position: absolute; left: 0; bottom: 0; width: 461px; height: 19px; }

  .booking {
    position: absolute; left: 30px; top: 0; width: 420px;
    font-family: "Source Sans 3", sans-serif; font-size: 13px; color: var(--ink-soft);
  }
  .booking__row { position: absolute; left: 0; width: 420px; height: 18px; }
  .booking__row:nth-child(1) { top: 97px; }
  .booking__row:nth-child(2) { top: 140px; }
  .booking__row:nth-child(3) { top: 181px; }
  .booking__label { position: absolute; top: 0; }
  .booking__rule { position: absolute; top: 14px; height: 1px; background: var(--rule); }
  .label-date { left: 0; }
  .rule-date { left: 40px; width: 162px; }
  .label-time { left: 212px; }
  .rule-time { left: 252px; width: 89px; }
  .label-ampm { left: 345px; }

  .booking__note {
    position: absolute; left: 0; right: 0; top: 228px; text-align: center;
    font-family: "Source Sans 3", sans-serif; font-style: italic; font-size: 11.5px; color: var(--ink-soft);
  }
</style>
</head>
<body>

<section class="card card--front" aria-label="Business card front">
  <div class="brand"><span class="brand__dot"></span><span>Marlowe<br>Chiropractic</span></div>

  <div class="person">
    <p class="person__name">Ted Marlowe, D.C.</p>
    <p class="person__title">Chiropractic physician</p>
  </div>

  <ul class="contact">
    <li class="contact__line">487 Keswick lane Suite 208</li>
    <li class="contact__line" style="margin-bottom:2px">Nashville, TN 48302</li>
    <li class="contact__line">
      <svg class="contact__icon" viewBox="0 0 12 12"><path d="M2.5 1h2l1 2.5-1.3 1a6 6 0 0 0 3.3 3.3l1-1.3 2.5 1v2c0 .6-.5 1-1 1A9.5 9.5 0 0 1 1.5 2c0-.5.4-1 1-1z" fill="#0d51a1"/></svg>
      555-482-1963</li>
    <li class="contact__line">
      <svg class="contact__icon" viewBox="0 0 12 12"><rect x="3" y="1" width="6" height="4" fill="#0d51a1"/><rect x="1" y="5" width="10" height="5" rx="1" fill="#0d51a1"/><rect x="3" y="8" width="6" height="3" fill="#fff"/></svg>
      555-482-7751</li>
    <li class="contact__line">
      <svg class="contact__icon" viewBox="0 0 12 12"><rect x="0.5" y="2.5" width="11" height="7.5" fill="#0d51a1"/><path d="M1 3l5 4 5-4" stroke="#fff" fill="none"/></svg>
      Drtedmarlowe@mailbox-example.com</li>
    <li class="contact__line">
      <svg class="contact__icon" viewBox="0 0 12 12"><circle cx="6" cy="6" r="5.5" fill="#0d51a1"/><ellipse cx="6" cy="6" rx="2.3" ry="5.3" fill="none" stroke="#fff" stroke-width="0.8"/><path d="M0.8 6h10.4" stroke="#fff" stroke-width="0.8"/></svg>
      www.MarloweChiropractic-example.com</li>
  </ul>

  <div class="portrait" role="img" aria-label="Portrait photo of Dr. Ted Marlowe in a light blue shirt and tie"></div>

  <svg class="band" viewBox="0 0 461 19" preserveAspectRatio="none">
    <polygon points="0,0 285,0 280,19 0,19" fill="var(--band-blue)"/>
    <polygon points="287,0 461,0 461,19 282,19" fill="var(--band-green)"/>
  </svg>
</section>

<section class="card card--back" aria-label="Business card back">
  <div class="brand"><span class="brand__dot"></span><span>Marlowe<br>Chiropractic</span></div>

  <div class="booking">
    <div class="booking__row">
      <span class="booking__label label-date">Date</span><span class="booking__rule rule-date"></span>
      <span class="booking__label label-time">Time</span><span class="booking__rule rule-time"></span>
      <span class="booking__label label-ampm">am/pm</span>
    </div>
    <div class="booking__row">
      <span class="booking__label label-date">Date</span><span class="booking__rule rule-date"></span>
      <span class="booking__label label-time">Time</span><span class="booking__rule rule-time"></span>
      <span class="booking__label label-ampm">am/pm</span>
    </div>
    <div class="booking__row">
      <span class="booking__label label-date">Date</span><span class="booking__rule rule-date"></span>
      <span class="booking__label label-time">Time</span><span class="booking__rule rule-time"></span>
      <span class="booking__label label-ampm">am/pm</span>
    </div>
  </div>

  <p class="booking__note">Please give 24 hours notice cancelling your appointment or a fee may be charged</p>
</section>

</body>
</html>
```